Catalogue des écoles de langues partenaires de Morvaleck

Who are we ?
The group has 3 Morvaleck training facilities that could be established in Tunisia in recent years: Morvaleck, Bristane and Pluvemor.
What do we offer?
A wide range of services for all those interested in the German language training, career counseling, translation, assitance start ... The Morvaleck group offers help at every stage.
We need a new 2016 catalog of language schools Morvaleck partners in our business.
This is based on the old catalog 2015, but with some modifications, including the Design level, catalog text and the list of partner schools that will be updated.
The idea is to make this catalog a guide that comes in direct contact with the customer that will read the catalog.
The purpose of this catalog is to create a direct relationship with the customer who will read to choose later the city and school that suit him.
The catalog contains roughly 3/4 sections:
* 1st section: the first pages "standards" of our brochure, here we leave the old model to add a few details and change the design and organization;
the logo, the German flag, catalog name, address for making contact with Morvaleck,
the summary, the map of Germany with cities on the departments where Morvaleck has partner schools
All this will not fail in our catalog
*2nd section:
Presentation cities where Morvaleck partner language schools are located
Here is a description of the city, pictures of the city and language schools list without going into details of each school
3rd section:
Part 1: Overview of language schools partner Morvaleck by our "guide" team that will accompany us in this section, there will be a representative from each school that is located in several cities
An overview of the school, the services (we leave the old model), the location of the school in every German city (google map photo), housing highlighted !!!!
The cultural prog perhaps?
Part 2: everything about the course:
max number of people in each class levels (page 3 of the old model), review KLO Centre or not, units per week, intensive courses, super intensive courses, prices ???course dates,
dsh - daf difference? Registration tips, links, ... a few tips
Quote " Ubung macht den Meister " for example
* 4th section and last section:
under the title of "1st Steps in Germany"
* What to do upon arrival
* Basic vocabulary (discussion circle, representatives from each school)
* Say goodbye, good luck .. Germany, photo, dream, travel ..
> Sayings of the whole team and bubbles!!!!
> We would like a design in shades of green of our logo !! (really important)
We take the example of a page of this catalog in this section.
The page consists of several parts:
School description, super intensive and intensive courses
Date of the beginning and the end of each session in this school
School Location (pictured google map)
A table that includes:
Room, kitchen, linen and towels, common area, distance to campus , the prices ,units per week
(See attached file )

```html
<!DOCTYPE html>
<html lang="fr">
<head>
<meta charset="utf-8">
<title>Wendhoff Berlin – Morvaleck</title>
<link rel="stylesheet" href="https://fonts.googleapis.com/css2?family=Montserrat:wght@400;600&family=Open+Sans:wght@400;600;700&display=swap">
<style>
  :root {
    --lime: #c6c91f;
    --lime-pale: #f6f2cf;
    --charcoal: #3b3b3b;
    --mist: #ececec;
    --paper: #ffffff;
    --backdrop: #e4e4e4;
    --ink: #3a3a3a;
    --rule: #cfcfcf;
  }
  * { box-sizing: border-box; margin: 0; padding: 0; }
  html, body { width: 1200px; height: 960px; overflow: hidden; }
  body { background: var(--backdrop); font-family: "Open Sans", sans-serif; color: var(--ink); }

  .flyer {
    position: absolute; left: 290px; top: 42px;
    width: 620px; height: 877px; background: var(--paper);
    overflow: hidden;
  }

  /* intro block */
  .intro {
    position: absolute; left: 0; top: 0; width: 384px; height: 335px;
    background: var(--lime); padding: 58px 28px 0 34px;
  }
  .intro-title {
    font-family: "Montserrat", sans-serif; font-weight: 400;
    font-size: 24px; letter-spacing: 0.5px; color: var(--paper);
    margin-bottom: 18px;
  }
  .intro-title .city { color: var(--charcoal); }
  .points { list-style: none; }
  .point {
    position: relative; padding-left: 26px; margin-bottom: 14px;
    font-size: 8.4px; line-height: 1.35; color: var(--ink);
  }
  .point svg { position: absolute; left: 0; top: 6px; }

  /* dates */
  .dates {
    position: absolute; left: 0; top: 335px; width: 384px; height: 92px;
    background: var(--mist); padding: 16px 34px 0 80px;
  }
  .dates-title {
    font-family: "Montserrat", sans-serif; font-weight: 400;
    font-size: 16px; color: var(--lime); margin-bottom: 6px;
  }
  .date-line {
    font-size: 8px; padding: 3px 0; border-bottom: 1px solid #9a9a9a;
  }

  .map {
    position: absolute; left: 0; top: 427px; width: 384px; height: 178px;
    background: linear-gradient(135deg, #e6e7d6, #d6e0c4 45%, #ece6d0);
  }

  /* contact band */
  .contact-band {
    position: absolute; left: 0; top: 605px; width: 384px; height: 62px;
    background: var(--charcoal); color: var(--paper);
    display: flex; align-items: center; justify-content: space-around;
    font-size: 13px;
  }
  .contact-item { display: flex; align-items: center; gap: 12px; }

  .photo-student {
    position: absolute; left: 0; top: 667px; width: 384px; height: 210px;
    background: linear-gradient(90deg, #6f8a5c, #b68aa0 35%, #4d6a3a 60%, #6fa6c9);
  }

  /* right column */
  .brand {
    position: absolute; left: 384px; top: 34px; width: 236px;
    display: flex; align-items: center; justify-content: center; gap: 8px;
    font-family: "Open Sans", sans-serif; font-weight: 700; font-size: 20px; color: var(--charcoal);
  }
  .brand-dot { width: 16px; height: 16px; border-radius: 50%; background: var(--lime); }

  .lodging {
    position: absolute; left: 404px; width: 198px;
    border-collapse: collapse; font-size: 8px;
  }
  .lodging.first { top: 104px; }
  .lodging.second { top: 352px; }
  .lodging th {
    background: var(--lime); color: var(--charcoal); font-weight: 700;
    text-align: left; padding: 4px 5px; height: 30px; vertical-align: top;
    border-right: 1px solid var(--paper);
  }
  .lodging td {
    height: 16px; border-right: 1px solid var(--rule); border-bottom: 1px solid var(--paper);
  }
  .lodging tr:nth-child(odd) td { background: var(--lime-pale); }
  .lodging td:last-child, .lodging th:last-child { border-right: none; }

  .mail-band {
    position: absolute; left: 384px; top: 588px; width: 236px; height: 50px;
    background: var(--lime); color: var(--paper);
    display: flex; align-items: center; gap: 14px; padding-left: 30px; font-size: 12px;
  }
  .photo-classroom {
    position: absolute; left: 384px; top: 638px; width: 236px; height: 239px;
    background: linear-gradient(160deg, #9b7a58, #d9d7cf 45%, #8e8a86);
  }
</style>
</head>
<body>
<main class="flyer">
  <section class="intro">
    <h1 class="intro-title">WENDHOFF <span class="city">BERLIN</span></h1>
    <ul class="points">
      <li class="point"><svg width="11" height="11" viewBox="0 0 11 11"><circle cx="5.5" cy="5.5" r="5.5" fill="#fff"/><path d="M3 5.5h5M6 3.5l2 2-2 2" stroke="#c6c91f" stroke-width="1.3" fill="none"/></svg>Nunc non volutpat dui, ut sollicitudin urna. Fusce laoreet tempor rhoncus. Sed egestas ultricies enim, vel faucibus mauris dignissim in. Sed in magna non quam condimentum congue. Curabitur feugiat dui nunc phasellus mauris. Necessitatibus saepe eveniet ut et voluptates.</li>
      <li class="point"><svg width="11" height="11" viewBox="0 0 11 11"><circle cx="5.5" cy="5.5" r="5.5" fill="#fff"/><path d="M3 5.5h5M6 3.5l2 2-2 2" stroke="#c6c91f" stroke-width="1.3" fill="none"/></svg>Nunc non volutpat dui, ut sollicitudin urna. Fusce laoreet tempor rhoncus. Sed egestas ultricies enim, vel faucibus mauris dignissim in. Sed in magna non quam condimentum congue. Curabitur feugiat dui nunc phasellus mauris. Necessitatibus saepe eveniet ut et voluptates.</li>
      <li class="point"><svg width="11" height="11" viewBox="0 0 11 11"><circle cx="5.5" cy="5.5" r="5.5" fill="#fff"/><path d="M3 5.5h5M6 3.5l2 2-2 2" stroke="#c6c91f" stroke-width="1.3" fill="none"/></svg>Nunc non volutpat dui, ut sollicitudin urna. Fusce laoreet tempor rhoncus. Sed egestas ultricies enim, vel faucibus mauris dignissim in. Sed in magna non quam condimentum congue. Curabitur feugiat dui nunc phasellus mauris.</li>
      <li class="point"><svg width="11" height="11" viewBox="0 0 11 11"><circle cx="5.5" cy="5.5" r="5.5" fill="#fff"/><path d="M3 5.5h5M6 3.5l2 2-2 2" stroke="#c6c91f" stroke-width="1.3" fill="none"/></svg>Nunc non volutpat dui, ut sollicitudin urna. Fusce laoreet tempor rhoncus. Sed egestas ultricies enim, vel faucibus mauris dignissim in. Sed in magna non quam condimentum congue. Curabitur feugiat dui nunc phasellus mauris.</li>
    </ul>
  </section>

  <section class="dates">
    <h2 class="dates-title">DATES DES COURSE 2015</h2>
    <p class="date-line">Nunc non volutpat dui, ut sollicitudin urna. Fusce laoreet</p>
    <p class="date-line">Nunc non volutpat dui, ut sollicitudin urna. Fusce laoreet</p>
    <p class="date-line">Nunc non volutpat dui, ut sollicitudin urna. Fusce laoreet</p>
  </section>

  <div class="map" role="img" aria-label="Street map showing the school's location in Berlin"></div>

  <section class="contact-band">
    <div class="contact-item">
      <svg width="24" height="24" viewBox="0 0 24 24"><circle cx="12" cy="12" r="11" fill="none" stroke="#fff" stroke-width="1.3"/><rect x="8.5" y="6" width="7" height="11" rx="3.5" fill="#fff"/><line x1="12" y1="7" x2="12" y2="10" stroke="#3b3b3b" stroke-width="1"/></svg>
      <span>www.morvaleck.org</span>
    </div>
    <div class="contact-item">
      <svg width="24" height="24" viewBox="0 0 24 24"><circle cx="12" cy="12" r="11" fill="none" stroke="#fff" stroke-width="1.3"/><path d="M8 7c-1 1-1 3 1 6s4 4 5.5 4.5c1 .3 2-.3 2.5-1l-2-2-1.3 1c-1-.5-2.7-2.2-3.2-3.2l1-1.3-2-2z" fill="#fff"/></svg>
      <span>71480362</span>
    </div>
  </section>

  <div class="photo-student" role="img" aria-label="Photo of a smiling student holding notebooks, with students walking behind"></div>

  <div class="brand"><span class="brand-dot"></span>Morvaleck</div>

  <table class="lodging first">
    <tr><th>wendhoff<br>berlin</th><th>Famille</th><th>Collocation</th></tr>
    <tr><td></td><td></td><td></td></tr><tr><td></td><td></td><td></td></tr>
    <tr><td></td><td></td><td></td></tr><tr><td></td><td></td><td></td></tr>
    <tr><td></td><td></td><td></td></tr><tr><td></td><td></td><td></td></tr>
    <tr><td></td><td></td><td></td></tr><tr><td></td><td></td><td></td></tr>
    <tr><td></td><td></td><td></td></tr><tr><td></td><td></td><td></td></tr>
    <tr><td></td><td></td><td></td></tr><tr><td></td><td></td><td></td></tr>
  </table>

  <table class="lodging second">
    <tr><th>wendhoff<br>berlin</th><th>Famille</th><th>Collocation</th></tr>
    <tr><td></td><td></td><td></td></tr><tr><td></td><td></td><td></td></tr>
    <tr><td></td><td></td><td></td></tr><tr><td></td><td></td><td></td></tr>
    <tr><td></td><td></td><td></td></tr><tr><td></td><td></td><td></td></tr>
    <tr><td></td><td></td><td></td></tr><tr><td></td><td></td><td></td></tr>
    <tr><td></td><td></td><td></td></tr><tr><td></td><td></td><td></td></tr>
    <tr><td></td><td></td><td></td></tr>
  </table>

  <section class="mail-band">
    <svg width="24" height="24" viewBox="0 0 24 24"><circle cx="12" cy="12" r="11" fill="none" stroke="#fff" stroke-width="1.3"/><rect x="6.5" y="8" width="11" height="8" fill="#fff"/><path d="M6.5 8l5.5 4.5L17.5 8" stroke="#c6c91f" stroke-width="1" fill="none"/></svg>
    <span>info.morvaleck.org</span>
  </section>

  <div class="photo-classroom" role="img" aria-label="Photo of a classroom with students seated at desks listening to a teacher"></div>
</main>
</body>
</html>
```